Website Landing Page for Medical Recruitment

Looking for a landing page to add to our existing website. The objective of the page is to recruit new clinical staff for various departments within Larkfield Medical Center (non-profit hospital in the Richmond, TX area).

We would like the page to be modern, professional, and non-cluttered. Please include call-to-actions and include a button that will navigate to the page where candidates can submit their applications (this page already exists).

Target Market(s)

25-35-year-olds who live in the Houston and Richmond area with medical experience.

Industry/Entity Type

Medical/Health

Font styles to use
Sans Serif

Colors
0054AA
0677BA
7BADD7
CADEEF
E8F1F8

Requirements
Must have
• A "call to action"; a button that navigates to larkfieldmedhub.example/careers

```html
<!DOCTYPE html>
<html lang="en">
<head>
<meta charset="utf-8">
<title>Recruitment | Larkfield Medical Center</title>
<link href="https://fonts.googleapis.com/css2?family=Open+Sans:wght@400;600;700&display=swap" rel="stylesheet">
<style>
:root{
  --accent:#17b3cf;
  --blue:#0054AA;
  --blue-mid:#0677BA;
  --blue-soft:#7BADD7;
  --blue-pale:#CADEEF;
  --blue-wash:#E8F1F8;
  --ink:#2b3138;
  --text:#555c64;
  --muted:#8a9098;
  --line:#e6e9ee;
  --panel:#f6f8fa;
  --band:#2c323a;
  --footer:#20252c;
  --footer-text:#9aa1aa;
  --white:#ffffff;
}
*{box-sizing:border-box;margin:0;padding:0}
html,body{width:1200px;height:3076px;overflow:hidden}
body{font-family:"Open Sans",Arial,sans-serif;color:var(--text);background:var(--white);position:relative;font-size:15px;line-height:1.6}
a{color:inherit;text-decoration:none}
.btn{display:inline-block;background:var(--accent);color:var(--white);font-size:12px;font-weight:700;letter-spacing:1px;text-transform:uppercase;padding:11px 26px;border-radius:2px}
.btn .arr{margin-left:6px}
.eyebrow{color:var(--accent);font-size:12px;letter-spacing:2px;text-transform:uppercase;font-weight:600}
.title{color:var(--ink);font-size:38px;font-weight:600;line-height:1.2}

/* top bar */
.topbar{position:absolute;top:0;left:0;width:1200px;height:40px;background:var(--white);border-bottom:1px solid var(--line);display:flex;align-items:center;padding:0 24px;font-size:12px;color:var(--muted);gap:24px}
.topbar .links{margin-left:auto;display:flex;gap:18px}
.topbar .links .pill{background:var(--blue);color:var(--white);padding:2px 10px;border-radius:2px}
.topbar svg{vertical-align:-2px;margin-right:4px}

/* header */
.header{position:absolute;top:40px;left:0;width:1200px;height:72px;display:flex;align-items:center;padding:0 24px;border-bottom:1px solid var(--line)}
.brand{display:flex;align-items:center;gap:10px;color:var(--blue);font-weight:700;font-size:18px;line-height:1.1}
.brand .dot{width:14px;height:14px;background:var(--blue);border-radius:50%}
.nav{margin-left:auto;display:flex;gap:24px;font-size:13px;color:var(--ink);align-items:center}
.nav .active{color:var(--accent)}
.nav .alert{color:#d23b3b}

/* hero */
.hero{position:absolute;top:112px;left:0;width:1200px;height:480px;background:linear-gradient(90deg,#8a9aa8 0%,#c7d3dc 35%,#d9e1e7 60%,#9fb0bd 100%);text-align:center;color:var(--white)}
.hero .shade{position:absolute;inset:0;background:rgba(20,40,60,.25)}
.hero .inner{position:relative;padding-top:120px}
.hero h1{font-size:60px;font-weight:700;line-height:1.1}
.hero p{font-size:16px;margin:14px auto 26px;width:420px}

/* services */
.services{position:absolute;top:592px;left:0;width:1200px;height:800px;text-align:center}
.services .eyebrow{position:absolute;top:42px;width:100%}
.services .title{position:absolute;top:72px;width:100%}
.services .lead{position:absolute;top:132px;left:400px;width:400px;font-size:14px}
.grid{position:absolute;top:228px;left:180px;width:840px;display:grid;grid-template-columns:repeat(3,280px);row-gap:50px}
.svc svg{width:56px;height:56px;display:block;margin:0 auto 12px}
.svc h3{color:var(--ink);font-size:17px;font-weight:600;margin-bottom:8px}
.svc p{font-size:13px;width:200px;margin:0 auto;line-height:1.5}
.services .btn{position:absolute;top:682px;left:528px}

/* why */
.why{position:absolute;top:1392px;left:0;width:1200px;height:488px;background:var(--panel)}
.why .copy{position:absolute;left:112px;top:106px;width:340px}
.why .title{margin:10px 0 24px}
.why .copy p{font-size:14px;margin-bottom:34px}
.why .frame-a{position:absolute;left:512px;top:88px;width:130px;height:380px;background:var(--accent)}
.why .frame-b{position:absolute;left:972px;top:88px;width:130px;height:80px;background:var(--accent)}
.why .photo{position:absolute;left:532px;top:104px;width:548px;height:360px;background:linear-gradient(100deg,#e4e9ee 0%,#f3f5f7 55%,#d6dee5 100%)}

/* faq */
.faq{position:absolute;top:1880px;left:0;width:1200px;height:600px;text-align:center}
.faq .eyebrow{position:absolute;top:40px;width:100%}
.faq .title{position:absolute;top:74px;width:100%;font-size:36px}
.faq .lead{position:absolute;top:146px;left:400px;width:400px;font-size:14px}
.accordion{position:absolute;top:250px;left:112px;width:976px;display:grid;grid-template-columns:476px 476px;column-gap:24px;row-gap:26px;text-align:left}
.q{height:64px;background:var(--panel);border:1px solid var(--line);display:flex;align-items:center;justify-content:space-between;padding:0 22px;color:var(--accent);font-size:14px;font-weight:600}

/* contact band */
.band{position:absolute;top:2480px;left:0;width:1200px;height:112px;background:var(--band);display:flex;align-items:center;padding-left:200px;gap:110px}
.band .item{display:flex;align-items:center;gap:14px;color:var(--white);font-size:13px;line-height:1.4}
.band .item small{display:block;color:var(--footer-text);font-size:11px}

/* footer */
.footer{position:absolute;top:2592px;left:0;width:1200px;height:440px;background:var(--footer);color:var(--footer-text);font-size:13px}
.footer h4{color:var(--white);font-size:15px;font-weight:600;margin-bottom:16px}
.social{position:absolute;left:112px;top:44px}
.social .widget{width:300px;height:180px;background:linear-gradient(180deg,#3b4652 0%,#4d5a66 45%,#e9ecef 45%,#f3f4f6 100%)}
.contact{position:absolute;left:624px;top:44px;width:300px}
.contact .addr{line-height:1.5;margin-bottom:18px}
.contact .lines{position:absolute;left:230px;top:44px;width:260px;line-height:2}
.contact .lines svg{vertical-align:-2px;margin-right:8px}
.contact .btn{margin-top:10px}

/* legal */
.legal{position:absolute;top:3032px;left:0;width:1200px;height:44px;background:var(--footer);border-top:1px solid #30363e;text-align:center;font-size:11px;color:var(--footer-text);padding-top:6px}
.cards{display:flex;gap:6px;justify-content:center;margin-top:2px}
.cards span{width:28px;height:16px;background:#d9dde2;border-radius:2px}
</style>
</head>
<body>

<div class="topbar">
  <span><svg width="12" height="12" viewBox="0 0 24 24" fill="none" stroke="currentColor" stroke-width="2"><path d="M12 22s7-7 7-12a7 7 0 0 0-14 0c0 5 7 12 7 12z"/><circle cx="12" cy="10" r="2.5"/></svg>480 Meadowline Avenue, Richmond, Texas</span>
  <span><svg width="12" height="12" viewBox="0 0 24 24" fill="none" stroke="currentColor" stroke-width="2"><path d="M5 3h4l2 5-3 2a11 11 0 0 0 6 6l2-3 5 2v4a2 2 0 0 1-2 2A17 17 0 0 1 3 5a2 2 0 0 1 2-2z"/></svg>(281) 555-0142</span>
  <div class="links"><a href="#">Careers</a><a href="#">Physician Staff Login</a><a href="#">Patient Portal</a><a href="#">Pay My Bill</a><a href="#">Contact Us</a><a class="pill" href="#">Larkfield Medical Group</a></div>
</div>

<header class="header">
  <div class="brand"><span class="dot"></span><span>Larkfield<br>Medical Center</span></div>
  <nav class="nav">
    <a class="active" href="#">Home</a><a href="#">Find a Doctor</a><a class="alert" href="#">COVID-19</a><a href="#">About Us</a><a href="#">Services</a><a href="#">Locations</a><a href="#">Patients/Visitors</a><a href="#">Ways To Give</a><a href="#">Health Library</a>
    <svg width="14" height="14" viewBox="0 0 24 24" fill="none" stroke="currentColor" stroke-width="2.5"><circle cx="10" cy="10" r="7"/><path d="M15 15l6 6"/></svg>
  </nav>
</header>

<section class="hero" role="img" aria-label="Photo of smiling clinical staff in scrubs and white coats">
  <div class="shade"></div>
  <div class="inner">
    <h1>Recruitment</h1>
    <p>We are hiring clinical staff in a variety of our departments. Join our team!</p>
    <a class="btn" href="https://larkfieldmedhub.example/careers">Apply For Job</a>
  </div>
</section>

<section class="services">
  <div class="eyebrow">Services</div>
  <h2 class="title">Available Services</h2>
  <p class="lead">Lorem ipsum dolor sit amet, consectetur adipiscing elit. Ut elit tellus, luctus nec ullamcorper mattis, pulvinar dapibus leo.</p>
  <div class="grid">
    <div class="svc">
      <svg viewBox="0 0 56 56" fill="none" stroke="var(--accent)" stroke-width="2"><rect x="8" y="10" width="40" height="28" rx="2"/><path d="M22 46h12M28 38v8M16 24h6l3-6 5 12 3-6h7"/></svg>
      <h3>Certified Nurses Assistants</h3><p>Lorem ipsum dolor sit amet, consectetur adipiscing elit.</p>
    </div>
    <div class="svc">
      <svg viewBox="0 0 56 56" fill="none" stroke="var(--accent)" stroke-width="2"><path d="M6 38V20h28v18M34 26h9l7 8v4H34"/><circle cx="16" cy="40" r="4"/><circle cx="40" cy="40" r="4"/><path d="M20 25v8M16 29h8"/></svg>
      <h3>Emergency Room Techs</h3><p>Lorem ipsum dolor sit amet, consectetur adipiscing elit.</p>
    </div>
    <div class="svc">
      <svg viewBox="0 0 56 56" fill="none" stroke="var(--accent)" stroke-width="2"><path d="M16 14h24l-3 10H19z"/><path d="M28 16v6M25 19h6"/><circle cx="28" cy="30" r="7"/><path d="M14 50c0-8 6-12 14-12s14 4 14 12"/></svg>
      <h3>Licensed Vocational Nurses</h3><p>Lorem ipsum dolor sit amet, consectetur adipiscing elit.</p>
    </div>
    <div class="svc">
      <svg viewBox="0 0 56 56" fill="none" stroke="var(--accent)" stroke-width="2"><circle cx="28" cy="20" r="8"/><path d="M12 50c0-9 7-14 16-14s16 5 16 14"/><path d="M28 40v6M25 43h6"/></svg>
      <h3>Registered Nurses</h3><p>Lorem ipsum dolor sit amet, consectetur adipiscing elit.</p>
    </div>
    <div class="svc">
      <svg viewBox="0 0 56 56" fill="none" stroke="var(--accent)" stroke-width="2"><rect x="12" y="10" width="32" height="40" rx="2"/><path d="M22 10v-3h12v3M20 22h16M20 30h16M20 38h10"/></svg>
      <h3>Unit Secretaries</h3><p>Lorem ipsum dolor sit amet, consectetur adipiscing elit.</p>
    </div>
    <div class="svc">
      <svg viewBox="0 0 56 56" fill="none" stroke="var(--accent)" stroke-width="2"><path d="M8 48V22l20-12 20 12v26z"/><path d="M28 24v14M21 31h14"/></svg>
      <h3>and more</h3><p>Lorem ipsum dolor sit amet, consectetur adipiscing elit.</p>
    </div>
  </div>
  <a class="btn" href="https://larkfieldmedhub.example/careers">Apply For Job</a>
</section>

<section class="why">
  <div class="copy">
    <div class="eyebrow">Benefits</div>
    <h2 class="title">Why Choose Us?</h2>
    <p>Lorem ipsum dolor sit amet, consectetur adipiscing elit. Ut elit tellus, luctus nec ullamcorper mattis, pulvinar dapibus leo.</p>
    <a class="btn" href="https://larkfieldmedhub.example/careers">Apply For Job</a>
  </div>
  <div class="frame-a"></div>
  <div class="frame-b"></div>
  <div class="photo" role="img" aria-label="Photo of a nurse holding a blue clipboard in a bright hospital corridor"></div>
</section>

<section class="faq">
  <div class="eyebrow">FAQ</div>
  <h2 class="title">Frequently Ask Questions</h2>
  <p class="lead">Lorem ipsum dolor sit amet, consectetur adipiscing elit. Ut elit tellus, luctus nec ullamcorper mattis, pulvinar dapibus leo.</p>
  <div class="accordion">
    <div class="q">Lorem ipsum dolor sit amet, consectetur adipiscing elit<svg width="12" height="8" viewBox="0 0 12 8" fill="none" stroke="var(--accent)" stroke-width="2"><path d="M1 1l5 5 5-5"/></svg></div>
    <div class="q">Lorem ipsum dolor sit amet, consectetur adipiscing elit<svg width="12" height="8" viewBox="0 0 12 8" fill="none" stroke="var(--accent)" stroke-width="2"><path d="M1 1l5 5 5-5"/></svg></div>
    <div class="q">Lorem ipsum dolor sit amet, consectetur adipiscing elit<svg width="12" height="8" viewBox="0 0 12 8" fill="none" stroke="var(--accent)" stroke-width="2"><path d="M1 1l5 5 5-5"/></svg></div>
    <div class="q">Lorem ipsum dolor sit amet, consectetur adipiscing elit<svg width="12" height="8" viewBox="0 0 12 8" fill="none" stroke="var(--accent)" stroke-width="2"><path d="M1 1l5 5 5-5"/></svg></div>
    <div class="q">Lorem ipsum dolor sit amet, consectetur adipiscing elit<svg width="12" height="8" viewBox="0 0 12 8" fill="none" stroke="var(--accent)" stroke-width="2"><path d="M1 1l5 5 5-5"/></svg></div>
    <div class="q">Lorem ipsum dolor sit amet, consectetur adipiscing elit<svg width="12" height="8" viewBox="0 0 12 8" fill="none" stroke="var(--accent)" stroke-width="2"><path d="M1 1l5 5 5-5"/></svg></div>
    <div class="q">Lorem ipsum dolor sit amet, consectetur adipiscing elit<svg width="12" height="8" viewBox="0 0 12 8" fill="none" stroke="var(--accent)" stroke-width="2"><path d="M1 1l5 5 5-5"/></svg></div>
    <div class="q">Lorem ipsum dolor sit amet, consectetur adipiscing elit<svg width="12" height="8" viewBox="0 0 12 8" fill="none" stroke="var(--accent)" stroke-width="2"><path d="M1 1l5 5 5-5"/></svg></div>
  </div>
</section>

<section class="band">
  <div class="item"><svg width="30" height="30" viewBox="0 0 24 24" fill="none" stroke="var(--white)" stroke-width="1.5"><path d="M5 3h4l2 5-3 2a11 11 0 0 0 6 6l2-3 5 2v4a2 2 0 0 1-2 2A17 17 0 0 1 3 5a2 2 0 0 1 2-2z"/></svg><div>(281) 555-0142<small>Call Us for more information</small></div></div>
  <div class="item"><svg width="30" height="30" viewBox="0 0 24 24" fill="none" stroke="var(--white)" stroke-width="1.5"><rect x="3" y="5" width="18" height="14" rx="1"/><path d="M3 6l9 7 9-7"/></svg><div>info@larkfieldmedhub.example<small>Send us a message</small></div></div>
  <div class="item"><svg width="30" height="30" viewBox="0 0 24 24" fill="none" stroke="var(--white)" stroke-width="1.5"><path d="M12 22s7-7 7-12a7 7 0 0 0-14 0c0 5 7 12 7 12z"/><circle cx="12" cy="10" r="2.5"/></svg><div>Visit our Location<small>480 Meadowline Avenue, Richmond, Texas</small></div></div>
</section>

<footer class="footer">
  <div class="social">
    <h4>Follow Us</h4>
    <div class="widget" role="img" aria-label="Embedded social page preview for Larkfield Medical Center"></div>
  </div>
  <div class="contact">
    <h4>Contact Details</h4>
    <p class="addr">Larkfield Medical Center<br>Meadowline Hospital Campus<br>480 Meadowline Avenue, Richmond</p>
    <div class="lines">
      <div><svg width="12" height="12" viewBox="0 0 24 24" fill="none" stroke="currentColor" stroke-width="2"><path d="M5 3h4l2 5-3 2a11 11 0 0 0 6 6l2-3 5 2v4a2 2 0 0 1-2 2A17 17 0 0 1 3 5a2 2 0 0 1 2-2z"/></svg>(281) 555-0142</div>
      <div><svg width="12" height="12" viewBox="0 0 24 24" fill="none" stroke="currentColor" stroke-width="2"><rect x="3" y="5" width="18" height="14"/><path d="M3 6l9 7 9-7"/></svg>info@larkfieldmedhub.example</div>
      <div><svg width="12" height="12" viewBox="0 0 24 24" fill="none" stroke="currentColor" stroke-width="2"><rect x="3" y="5" width="18" height="14"/><path d="M3 6l9 7 9-7"/></svg>careers@larkfieldmedhub.example</div>
      <div><svg width="12" height="12" viewBox="0 0 24 24" fill="none" stroke="currentColor" stroke-width="2"><circle cx="12" cy="12" r="9"/><path d="M3 12h18M12 3c3 3 3 15 0 18"/></svg>larkfieldmedhub.example</div>
    </div>
    <a class="btn" href="#">Get Map Directions <span class="arr">→</span></a>
  </div>
</footer>

<div class="legal">
  Copyright Larkfield 2021 | Website by Northgate Web Studio | Privacy Policy | Refund Policy | Public Information Request
  <div class="cards"><span></span><span></span><span></span><span></span><span></span></div>
</div>

</body>
</html>
```